Geschäftspapier-Design für Anbieter einer Online-Ausbildung für den qualifizierten Krankentransport und Rettungsdienst
Zielgruppe
LOTH Online-Ausbildung für den qualifizierten Krankentransport und Rettungsdienst
Der qualifizierte Krankentransport und Rettungsdienst ist zuständig für den Transport- und die Versorgung von kranken und verletzten Menschen. LOTH Medizinische Ausbildung und Seminare hat sich als Privatschule für die präklinische Notfallmedizin auf Aus- und Weiterbildungen im E-Learning-Modul für diese zwei Fachbereiche spezialisiert. Alle unsere Fachausbildungen sind online in unserem modernen Campus mit überregionalem Zugang absolvierbar.
Aufgabenstellung
Wir benötigen eine Word-Briefvorlage für den alltäglichen Geschäftsverkehr in drei Ausführungen.
- Briefvorlage mit Angabe der Abteilung -> Sekretariat
- Briefvorlage mit Angabe der Abteilung -> Schulleitung
- Briefvorlage mit Angabe der Abteilung -> Geschäftsführung
- Briefvorlage mit Angabe der Abteilung -> Buchhaltung/ Forderungsmanagement
Die Vorlage sollte bitte folgende Angaben aufweisen:
LOTH Bildungsgesellschaft UG (haftungsbeschränkt)
Privatschule für prähospitale Rettungsmedizin
Standort unserer Verwaltung:
Farnhügel 7
15537 Erkner
Standort unseres Schulsitzes:
Am Quendelhof 48
D- 15537 Gosen- Neu Zittau
Schulleitung: Jutta Wildgrube & Matthias Lot
Ärztliche Leitung: Dr. Med. Ortwin Brasch
Pädagogische Leitung: Matthias Loth
Fachlicher Beirat: Dr. rer. med. Fabian Oswalt
Tel: 030 6270384 50
Fax: 030 6270384 51
E-Mail: info@loth-lehrwerkstatt.de
Web: www.loth-lehrwerkstatt.de
Vertreten durch: Jutta Wildgrube
Registereintrag: Eintragung im Handelsregister Registergericht: Amtsgericht Frankfurt (Oder) Registernummer: HRB 27403 FF

```html
<!DOCTYPE html>
<html lang="de">
<head>
<meta charset="utf-8">
<title>LOTH Bildungsgesellschaft – Folgeblatt</title>
<link rel="stylesheet" href="https://fonts.googleapis.com/css2?family=Source+Sans+3:wght@400;600&display=swap">
<style>
  :root {
    --brand-blue: #6ca5d5;
    --ink: #1d1d1b;
    --rule: #1d1d1b;
    --paper: #ffffff;
  }
  * { margin: 0; padding: 0; box-sizing: border-box; }
  html, body {
    width: 862px;
    height: 1200px;
    overflow: hidden;
    background: var(--paper);
  }
  .letterhead {
    position: relative;
    width: 862px;
    height: 1200px;
    font-family: "Source Sans 3", "Myriad Pro", sans-serif;
    color: var(--ink);
  }
  .page-frame {
    position: absolute;
    left: 37px;
    top: 43px;
    width: 786px;
    height: 1111px;
    border: 1px solid var(--rule);
  }
  .band {
    position: absolute;
    left: 37px;
    width: 786px;
    height: 15px;
    background: var(--brand-blue);
  }
  .band--top { top: 58px; }
  .band--bottom { top: 1124px; }
  .hairline {
    position: absolute;
    left: 37px;
    width: 786px;
    height: 1px;
    background: var(--rule);
  }
  .hairline--top { top: 78px; }
  .hairline--bottom { top: 1118px; }
  .fold-mark {
    position: absolute;
    left: 37px;
    width: 15px;
    height: 1px;
    background: var(--rule);
  }
  .fold-mark--upper { top: 435px; }
  .fold-mark--lower { top: 598px; }
  .sheet-label {
    position: absolute;
    left: 120px;
    top: 180px;
    font-size: 10px;
    font-weight: 400;
    letter-spacing: 0.01em;
  }
  .brand-name {
    position: absolute;
    left: 498px;
    top: 135px;
    font-size: 34px;
    font-weight: 600;
    line-height: 1;
    color: var(--brand-blue);
    letter-spacing: 0.02em;
  }
  .brand-divider {
    position: absolute;
    left: 590px;
    top: 104px;
    width: 1px;
    height: 110px;
    background: var(--brand-blue);
  }
  .brand-lines {
    position: absolute;
    left: 597px;
    top: 126px;
    font-size: 12.6px;
    font-weight: 600;
    line-height: 16px;
  }
  .brand-lines .company { margin-bottom: 4px; }
</style>
</head>
<body>
  <main class="letterhead">
    <div class="page-frame"></div>
    <div class="band band--top"></div>
    <div class="hairline hairline--top"></div>

    <p class="sheet-label">Folgeblatt</p>

    <div class="brand-name">LOTH</div>
    <div class="brand-divider"></div>
    <div class="brand-lines">
      <p class="company">LOTH Bildungsgesellschaft UG<br>(haftungsbeschränkt)</p>
      <p class="tagline">Privatschule für<br>prähospitale Rettungsmedizin</p>
    </div>

    <div class="fold-mark fold-mark--upper"></div>
    <div class="fold-mark fold-mark--lower"></div>

    <div class="hairline hairline--bottom"></div>
    <div class="band band--bottom"></div>
  </main>
</body>
</html>
```